Tru Wave and Link post card design

We need a postcard to hand out to prospective clients detailing what we do with contact details kept to just a mobile phone number.
Tru Wave and Link is a communications networking company specialising in computer cabling, phone cabling, fibre optics, CCTV, particularly for small business. We offer licenced technicians with over 20 years experience in this field. We service greater Brisbane. Designs that incorporate colours from our logo would be great and that is similar to our business card.
Communications

```html
<!DOCTYPE html>
<html lang="en">
<head>
<meta charset="utf-8">
<title>Tru Wave and Link – Postcard</title>
<link href="https://fonts.googleapis.com/css2?family=Share+Tech+Mono&display=swap" rel="stylesheet">
<style>
  :root {
    --backdrop: #b9b9b7;
    --brand-green: #2b9e43;
    --brand-green-dark: #238a38;
    --card-white: #e8e8e6;
    --line-white: #ffffff;
    --label-black: #1b1b1b;
    --dash-olive: #a3a62a;
    --dash-green: #5f8f2f;
    --ink-green: #3f7f2c;
  }
  * { box-sizing: border-box; margin: 0; padding: 0; }
  html, body { width: 1200px; height: 768px; overflow: hidden; }
  body {
    background: var(--backdrop);
    font-family: "Share Tech Mono", monospace;
    position: relative;
  }
  .postcard {
    position: absolute;
    top: 199px;
    width: 540px;
    height: 370px;
    overflow: hidden;
    box-shadow: 0 8px 18px rgba(0,0,0,.28);
  }

  /* ---------- front ---------- */
  .postcard--front { left: 40px; background: var(--brand-green); color: var(--line-white); }
  .equipment-drawing {
    position: absolute; left: 0; top: 0; width: 118px; height: 100%;
    background: var(--brand-green-dark);
    border-right: 1.5px solid var(--line-white);
  }
  .front-rule {
    position: absolute; left: 118px; right: 0; height: 0;
    border-top: 1.5px solid var(--line-white);
  }
  .front-rule--top { top: 26px; }
  .front-rule--bottom { top: 314px; }
  .services { position: absolute; left: 150px; top: 40px; }
  .services__heading { font-size: 14px; letter-spacing: 2px; text-transform: uppercase; font-weight: 400; }
  .services__intro { font-size: 14px; letter-spacing: 2px; margin: 12px 0 12px 14px; }
  .services__list { list-style: none; }
  .services__list li { display: block; }
  .services__item {
    display: inline-block; background: var(--label-black);
    font-size: 16px; letter-spacing: 1.5px;
    padding: 2px 26px 2px 8px; margin-bottom: 10px; min-width: 170px;
  }
  .services__item--short { min-width: 0; padding-right: 12px; }
  .experience { font-size: 14px; letter-spacing: 1.5px; line-height: 1.45; margin-top: 4px; }
  .front-brand {
    position: absolute; right: 22px; bottom: 14px;
    font-size: 26px; letter-spacing: 1px; color: var(--line-white);
    display: flex; align-items: center; gap: 10px;
  }
  .front-brand__dot { width: 14px; height: 14px; border-radius: 50%; background: var(--line-white); }

  /* ---------- back ---------- */
  .postcard--back { left: 620px; background: var(--card-white); }
  .back-guides { position: absolute; inset: 0; }
  .back-brand {
    position: absolute; left: 30px; top: 30px;
    display: flex; align-items: center; gap: 10px;
    font-size: 26px; color: var(--brand-green);
  }
  .back-brand__dot { width: 16px; height: 16px; border-radius: 50%; background: var(--dash-olive); }
  .back-mobile {
    position: absolute; left: 32px; top: 68px;
    font-size: 13px; letter-spacing: 2px; color: var(--ink-green);
  }
  .recipient {
    position: absolute; left: 298px; top: 196px;
    font-style: normal; font-size: 17px; letter-spacing: 1.5px; line-height: 1.2;
    color: var(--ink-green);
  }
</style>
</head>
<body>

<section class="postcard postcard--front" aria-label="Postcard front">
  <div class="equipment-drawing" role="img" aria-label="Line drawing of a network cabling rack with connection points"></div>
  <div class="front-rule front-rule--top"></div>
  <div class="front-rule front-rule--bottom"></div>

  <div class="services">
    <h2 class="services__heading">Communications Networking</h2>
    <p class="services__intro">we specialize in</p>
    <ul class="services__list">
      <li><span class="services__item">computer cabling</span></li>
      <li><span class="services__item">phone cabling</span></li>
      <li><span class="services__item">fibre optics</span></li>
      <li><span class="services__item services__item--short">CCTV</span></li>
    </ul>
    <p class="experience">Technicians with over<br>20 years Experience!<br>small business, greater Brisbane</p>
  </div>

  <div class="front-brand"><span class="front-brand__dot"></span>Tru Wave and Link</div>
</section>

<section class="postcard postcard--back" aria-label="Postcard back">
  <svg class="back-guides" width="540" height="370" viewBox="0 0 540 370" aria-hidden="true">
    <g fill="none" stroke-width="3" stroke-dasharray="14 9">
      <line x1="0" y1="102" x2="210" y2="102" stroke="var(--dash-olive)"/>
      <line x1="150" y1="102" x2="150" y2="330" stroke="var(--dash-green)"/>
      <line x1="150" y1="330" x2="540" y2="330" stroke="var(--dash-green)"/>
      <rect x="406" y="36" width="98" height="98" stroke="var(--dash-green)"/>
    </g>
  </svg>

  <div class="back-brand"><span class="back-brand__dot"></span>Tru Wave and Link</div>
  <p class="back-mobile">mob 0491 570 156</p>

  <address class="recipient">
    Alex Reed<br>
    58 Harbour Lane<br>
    Brisbane, QLD<br>
    4000
  </address>
</section>

</body>
</html>
```